IT company website design

Require a home page and an inner page designed for a company located in Ohio. The company deals with a wide range of IT services like Software development, IT based education services such as digital textbooks and BPO

Would like to get a Home page for the website and an inner page to be designed.

Design must be modern, clean and very professional. The home page should have a carousel of our services for which content will be provided.

It should give a feel that we are a large company to our prospective customers.
Updates

Hi,
In the few designs I have got for the home page, there are mockups with unwanted content/blocks like ex. latest blog posts or similar blocks. Kindly note that, we don't want this. Please follow the information about content on the home page as mentioned in the project brief. Designers, who have already submitted designs, if you can remove the unwanted blocks, it will be really appreciated.

Thanks.

I have received over 9 designs for this project, but none of them seem to be custom designed for my needs. They are just re-use of previous designs and look very out dated. Looking for fresh, clean designs following latest design trends like the ones you see in gridmarket etc.

If you can provide me a design that meets my expectations, I can definitely UP my budget for you .

Industry/Entity Type

Education

Requirements
Must have
• > > Home page > >
Home page will have

* Top Menu: Home, About Us, Solutions, Services, Contact us (should have space to accommodate for more)

* Should have a flash carousel/slide show. Each slide should be about a service we provide. Ex. a slide for bpo will have the content "Bridging the quality and cost divide in outsourcing" It should be depicted by an illustration or photograph. If you are going to use photograph, please use ones for pixvaultimages.com

* Textual content of about 200 words which we will provide

* Links in the footer along with a copyright, legal notice etc.

* Importantly, the home page should have 2 fancy buttons for "Member Login" and "Online Tutoring"

> > Inner pages > >
Will be mainly textual content explaining each of the service so, should have space for lots of textual content, with a fancy, page title (usually the service name). All inner pages should also have a side menu or something like that from where users can have a one click access to all our services.

Our logo is blue in color. with color code "0080FB". It just a stylized D with rest of the text i.e Varnex Tek Inc. our logo is of the proportion. 1:5 i.e 60px height, 300px wide. We can proportionately increase or decrease the dimensions as necessary. Color combination of the sight should be something that will go with this.

```html
<!DOCTYPE html>
<html lang="en">
<head>
<meta charset="utf-8">
<title>Home</title>
<link rel="stylesheet" href="https://fonts.googleapis.com/css2?family=Arimo:wght@400;700&family=Open+Sans:wght@400;600&family=PT+Sans:wght@400;700&display=swap">
<style>
:root{
  --sky-top:#8ec8ff;
  --sky-mid:#5aaeff;
  --sky-deep:#1a86f5;
  --nav-blue:#0a7ff0;
  --page-grey:#eeeeee;
  --white:#ffffff;
  --ink:#1d1d1d;
  --logo-orange:#c4510e;
  --tag-olive:#7a6410;
  --accent-orange:#f08a3c;
  --login-orange:#f2661c;
  --tutor-yellow:#fbd978;
  --tutor-ink:#8a6a08;
  --footer-top:#2c2c2c;
  --footer-bottom:#4a4a4a;
  --footer-text:#f2f2f2;
  --footer-logo:#b9b9b9;
}
*{margin:0;padding:0;box-sizing:border-box}
html,body{width:1054px;height:1200px;overflow:hidden}
body{position:relative;background:var(--page-grey);font-family:"Arimo",Arial,sans-serif;color:var(--ink)}

.site-header{position:absolute;left:0;top:0;width:1054px;height:220px;
  background:radial-gradient(ellipse 60% 90% at 50% 25%,var(--sky-top),var(--sky-mid) 55%,var(--sky-deep));}

.quick-button{position:absolute;display:flex;flex-direction:column;justify-content:center;align-items:center;
  text-decoration:none;font-family:"PT Sans",sans-serif;text-align:center;border-radius:6px}
.quick-button .label{font-weight:700;font-size:22px;line-height:23px;letter-spacing:0.5px}
.quick-button .note{font-family:"Arimo",sans-serif;font-size:12px;margin-top:4px}
.member-login{left:136px;top:34px;width:170px;height:110px;background:var(--login-orange);color:var(--white)}
.online-tutoring{left:226px;top:120px;width:190px;height:100px;background:var(--tutor-yellow);color:var(--tutor-ink)}
.online-tutoring .note{color:#5a4a10}

.brand-box{position:absolute;left:468px;top:130px;width:412px;height:95px;background:var(--white);
  border-radius:7px 7px 0 0;text-align:center;font-family:"Open Sans",sans-serif}
.brand-name{display:block;margin-top:20px;font-size:31px;color:var(--logo-orange);letter-spacing:-0.5px}
.brand-tagline{display:block;font-size:14px;color:var(--tag-olive);margin-top:-4px}

.nav-band{position:absolute;left:0;top:220px;width:1054px;height:40px;
  background:linear-gradient(var(--white) 0 5px,#6fb7f6 5px,#2a8ef0 18px,var(--nav-blue) 22px,var(--nav-blue) 100%);}
.nav-band::after{content:"";position:absolute;left:0;right:0;bottom:0;height:6px;background:var(--white)}
.main-nav{position:absolute;top:232px;left:472px;display:flex;font-family:"PT Sans",sans-serif;font-weight:700;font-size:14px;color:var(--white);letter-spacing:0.3px}
.main-nav a{color:inherit;text-decoration:none;padding:0 15px;border-left:1px solid var(--accent-orange);line-height:22px}
.main-nav a:first-child{border-left:0;padding-left:0;padding-right:18px}
.nav-pointer{position:absolute;left:484px;top:224px;width:0;height:0;border-left:5px solid transparent;border-right:5px solid transparent;border-top:6px solid var(--white)}

.showcase{position:absolute;left:170px;top:299px;width:760px;height:291px;
  background:linear-gradient(110deg,#e9f4ff 0%,#9cc8ee 22%,#5d8fbf 45%,#3e6d9c 70%,#1d3350 100%)}
.slide-arrow{position:absolute;top:413px;width:64px;height:64px}
.slide-arrow.prev{left:168px}
.slide-arrow.next{left:864px}

.intro{position:absolute;left:0;top:651px;width:1054px;height:371px;
  background:radial-gradient(ellipse 65% 85% at 50% 45%,#b9dcff,#86c0ff 55%,#3b8ff7);
  box-shadow:0 0 14px rgba(0,0,0,.25)}
.intro-copy{position:absolute;left:172px;top:31px;width:756px}
.intro-copy p{font-size:17.6px;line-height:20.4px;margin-bottom:10px}
.intro-copy p.small{font-size:14.6px;line-height:20px}

.site-footer{position:absolute;left:0;top:1051px;width:1054px;height:149px;
  background:linear-gradient(var(--footer-top),var(--footer-bottom) 60%)}
.footer-brand{position:absolute;left:272px;top:22px;font-family:"Open Sans",sans-serif;font-size:60px;font-weight:600;color:var(--footer-logo);letter-spacing:-1px}
.footer-divider{position:absolute;left:470px;top:28px;height:84px;border-left:1px dotted #cfcfcf}
.footer-nav{position:absolute;left:494px;top:52px;font-family:"PT Sans",sans-serif;font-size:12.5px;color:var(--footer-text);display:flex}
.footer-nav a{color:inherit;text-decoration:none;padding:0 11px;border-left:1px solid var(--footer-text);line-height:12px}
.footer-nav a:first-child{border-left:0;padding-left:0}
.copyright{position:absolute;left:496px;top:77px;font-family:"PT Sans",sans-serif;font-size:11.5px;color:var(--accent-orange)}
</style>
</head>
<body>

<header class="site-header">
  <a class="quick-button member-login" href="#">
    <span class="label">MEMBER<br>LOGIN</span>
    <span class="note">Short description!</span>
  </a>
  <a class="quick-button online-tutoring" href="#">
    <span class="label">ONLINE<br>TUTORING</span>
    <span class="note">Short description!</span>
  </a>
  <div class="brand-box">
    <span class="brand-name">logo goes here</span>
    <span class="brand-tagline">tagline</span>
  </div>
</header>

<div class="nav-band"></div>
<span class="nav-pointer"></span>
<nav class="main-nav">
  <a href="#">Home</a><a href="#">About us</a><a href="#">Solutions</a><a href="#">Services</a><a href="#">Contact us</a>
</nav>

<div class="showcase" role="img" aria-label="Service slide photograph: software update screen with progress readouts"></div>
<svg class="slide-arrow prev" viewBox="0 0 64 64" aria-label="Previous slide">
  <circle cx="32" cy="32" r="30" fill="#b9c4cf" fill-opacity=".8" stroke="#8c99a6" stroke-width="2"/>
  <path d="M14 32 L28 19 V27 H49 V37 H28 V45 Z" fill="#fff"/>
</svg>
<svg class="slide-arrow next" viewBox="0 0 64 64" aria-label="Next slide">
  <circle cx="32" cy="32" r="30" fill="#6f93b4" fill-opacity=".85" stroke="#4f7395" stroke-width="2"/>
  <path d="M50 32 L36 19 V27 H15 V37 H36 V45 Z" fill="#d9ecff"/>
</svg>

<section class="intro">
  <div class="intro-copy">
    <p><b>Lorem ipsum dolor sit amet, consectetuer adipiscing elit. Nunc euis, libero vel interdum interdum,</b> neque sapien nonummy orci, ac sollicitudin ante urna a pede. Suspendisse hendrerit orci ut dui sollicitudin spendisseert venenatis.Utut leo vel orci dignissim pulvinar. Nam ut lacus nec tortor blandit tincidunt. Duis suscipit nunc vitae dolor lacinia hendrerit. Fusce orci lectusty porttitor suscipit, elementum eu, tincidunt vitae, felis. Proin nunc tortor,ender feugiat vel, gravida eu, congue vel, felis. In eget turpis. Curabitur ligula.Nunc arcu dolor, vulputate eu, porta in, porta in, lorem.</p>
    <p class="small"><b>Lorem ipsum dolor sit amet, consectetuer adipiscing elit. Nunc euis, libero vel interdum interdum,</b> neque sapien nonummy orci, ac sollicitudin ante urna a pede. Suspendisse hendrerit orci ut dui sollicitudin spendisseert venenatis.Utut leo vel orci dignissim pulvinar. Nam ut lacus nec tortor blandit tincidunt. Duis suscipit nunc vitae dolor lacinia hendrerit. Fusce orci lectusty porttitor suscipit, elementum eu, tincidunt vitae, felis. Proin nunc tortor,ender feugiat vel, gravida eu, congue vel, felis. In eget turpis. Curabitur ligula.Nunc arcu dolor, vulputate eu, porta in, porta in, lorem.</p>
  </div>
</section>

<footer class="site-footer">
  <span class="footer-brand">logo</span>
  <span class="footer-divider"></span>
  <nav class="footer-nav">
    <a href="#">Home</a><a href="#">About us</a><a href="#">Solutions</a><a href="#">Services</a><a href="#">Contact us</a>
  </nav>
  <p class="copyright">© all right reaserved</p>
</footer>

</body>
</html>
```